For Sale Sign for Real Estate Agency

We need a For Sale Sign designed for our agency. I want a very simple/elegant sign that says "For Sale" towards the top of the sign (not in huge letters). Most of the sign should be a design/picture with our name and phone number somewhere at the bottom.

One significant detail, it's important that our logo not be too big or the center piece of the sign. Since our company name has the word "rent" in it, people assume the house is for rent, instead of for sale.

I attached our logo and a rough outline of the format I'm looking for.

Again, I'm looking for elegant and simple! Thanks for your time

Industry/Entity Type

Real Estate

Colors

Designer to choose colors to be used in the design.

Requirements
Must have
Nice to have
Should not have
• Nothing tacky!
• Our logo/company name should not be too big or the center piece of the sign. Since our company name has the word "rent" in it, people assume the house is for rent, instead of for sale.

```html
<!DOCTYPE html>
<html lang="en">
<head>
<meta charset="utf-8">
<title>Kestrel Realty – For Sale Sign</title>
<link rel="stylesheet" href="https://fonts.googleapis.com/css2?family=Jost:wght@400;600&family=Arimo:wght@400&display=swap">
<style>
  :root {
    --paper: #ffffff;
    --ink: #000000;
    --brand-red: #c2321a;
    --sale-brown: #7a2408;
    --trim-line: #cfcfcf;
    --crop-mark: #555555;
    --logo-ink: #140805;
  }
  * { margin: 0; padding: 0; box-sizing: border-box; }
  html, body {
    width: 1200px; height: 620px; overflow: hidden; background: var(--paper);
  }
  .sheet {
    position: relative; width: 1500px; height: 775px;
    transform: scale(0.8); transform-origin: 0 0;
  }
  .sign { position: absolute; background: var(--paper); outline: 1px solid var(--trim-line); }
  .sign > * { position: absolute; }
  .crop { position: absolute; background: var(--crop-mark); }
  .crop.v { width: 1px; }
  .crop.h { height: 1px; }

  .band-black { background: var(--ink); }
  .band-red, .contact-box, .logo-box { background: var(--brand-red); }
  .skyline {
    background: linear-gradient(90deg, #8a6a4c 0%, #b79a86 10%, #a38fc2 22%, #c9a3b8 32%, #b8a89a 45%, #9a92c4 60%, #8d86c0 75%, #b6a38e 88%, #9c8a7a 100%);
  }
  .skyline::after {
    content: ""; position: absolute; left: 0; right: 0; bottom: 0; height: 30%;
    background: linear-gradient(180deg, rgba(40,40,60,0) 0%, rgba(30,35,50,.85) 100%);
  }
  .contact-box {
    font-family: "Arimo", Arial, sans-serif; color: var(--ink); line-height: 1.15;
  }
  .contact-box .phone { margin-top: 0.9em; }
  .wordmark {
    font-family: "Jost", sans-serif; font-weight: 400; color: var(--logo-ink);
    white-space: nowrap; text-align: right; line-height: 1;
  }
  .sale-tag {
    background: var(--sale-brown); color: var(--paper);
    font-family: "Jost", sans-serif; font-weight: 600; letter-spacing: 0.02em;
    display: flex; align-items: center; justify-content: center;
    box-shadow: -10px 12px 14px rgba(60, 50, 90, 0.35);
    white-space: nowrap;
  }

  /* Landscape sign */
  .sign--wide { left: 17px; top: 117px; width: 821px; height: 581px; }
  .sign--wide .band-black.mid { left: 0; top: 201px; width: 821px; height: 174px; }
  .sign--wide .contact-box { left: 676px; top: 275px; width: 145px; height: 98px; padding: 13px 0 0 15px; font-size: 12px; }
  .sign--wide .skyline { left: 0; top: 373px; width: 821px; height: 83px; }
  .sign--wide .band-red { left: 0; top: 456px; width: 676px; height: 63px; }
  .sign--wide .band-black.base { left: 0; top: 519px; width: 676px; height: 62px; }
  .sign--wide .logo-box { left: 676px; top: 463px; width: 145px; height: 118px; }
  .sign--wide .band-black.notch { left: 676px; top: 456px; width: 145px; height: 7px; }
  .sign--wide .wordmark { right: 20px; top: 486px; font-size: 40px; }
  .sign--wide .sale-tag { left: 125px; top: 70px; width: 540px; height: 155px; font-size: 96px; transform: rotate(-9.5deg); }

  /* Portrait sign */
  .sign--tall { left: 962px; top: 18px; width: 519px; height: 737px; }
  .sign--tall .band-black.mid { left: 0; top: 192px; width: 519px; height: 330px; }
  .sign--tall .contact-box { left: 389px; top: 419px; width: 130px; height: 103px; padding: 26px 0 0 14px; font-size: 11px; }
  .sign--tall .skyline { left: 0; top: 522px; width: 519px; height: 105px; }
  .sign--tall .band-red { left: 0; top: 627px; width: 389px; height: 55px; }
  .sign--tall .band-black.base { left: 0; top: 682px; width: 389px; height: 55px; }
  .sign--tall .logo-box { left: 389px; top: 632px; width: 130px; height: 105px; }
  .sign--tall .band-black.notch { left: 389px; top: 627px; width: 130px; height: 5px; }
  .sign--tall .wordmark { right: 20px; top: 652px; font-size: 34px; }
  .sign--tall .sale-tag { left: 50px; top: 69px; width: 418px; height: 125px; font-size: 78px; transform: rotate(-8.7deg); }
</style>
</head>
<body>
<div class="sheet">
  <!-- crop marks: landscape sign -->
  <span class="crop v" style="left:17px;top:97px;height:20px"></span>
  <span class="crop h" style="left:0;top:117px;width:17px"></span>
  <span class="crop v" style="left:838px;top:97px;height:20px"></span>
  <span class="crop h" style="left:838px;top:117px;width:20px"></span>
  <span class="crop v" style="left:17px;top:698px;height:20px"></span>
  <span class="crop h" style="left:0;top:698px;width:17px"></span>
  <span class="crop v" style="left:838px;top:698px;height:20px"></span>
  <span class="crop h" style="left:838px;top:698px;width:20px"></span>

  <!-- crop marks: portrait sign -->
  <span class="crop v" style="left:962px;top:0;height:18px"></span>
  <span class="crop h" style="left:942px;top:18px;width:20px"></span>
  <span class="crop v" style="left:1481px;top:0;height:18px"></span>
  <span class="crop h" style="left:1481px;top:18px;width:19px"></span>
  <span class="crop v" style="left:962px;top:755px;height:20px"></span>
  <span class="crop h" style="left:942px;top:755px;width:20px"></span>
  <span class="crop v" style="left:1481px;top:755px;height:20px"></span>
  <span class="crop h" style="left:1481px;top:755px;width:19px"></span>

  <section class="sign sign--wide" aria-label="Landscape for sale sign">
    <div class="band-black mid"></div>
    <div class="contact-box">
      <p>Kestrel Realty</p>
      <p>214 Marlowe Avenue</p>
      <p>Bristow, RI 02950</p>
      <p class="phone">(401) 555-0147</p>
    </div>
    <div class="skyline" role="img" aria-label="Panoramic city skyline at dusk with lit office towers and a clock tower"></div>
    <div class="band-red"></div>
    <div class="band-black base"></div>
    <div class="band-black notch"></div>
    <div class="logo-box"></div>
    <p class="wordmark">Kestrel Realty</p>
    <h1 class="sale-tag">FOR SALE</h1>
  </section>

  <section class="sign sign--tall" aria-label="Portrait for sale sign">
    <div class="band-black mid"></div>
    <div class="contact-box">
      <p>Kestrel Realty</p>
      <p>214 Marlowe Avenue</p>
      <p>Bristow, RI 02950</p>
      <p class="phone">(401) 555-0147</p>
    </div>
    <div class="skyline" role="img" aria-label="City skyline at dusk with high-rise towers under a violet sky"></div>
    <div class="band-red"></div>
    <div class="band-black base"></div>
    <div class="band-black notch"></div>
    <div class="logo-box"></div>
    <p class="wordmark">Kestrel Realty</p>
    <h2 class="sale-tag">FOR SALE</h2>
  </section>
</div>
</body>
</html>
```